Need a website built for a Home Care Agency Business

I need the website designed and implemented into Weebly or any suggested platform that you think will work better. A few websites that I like are: [login to view URL](this one being the best of them all), [login to view URL], [login to view URL], and https://www.quornest.com. No shopping card needed. The website must be mobile friendly. Landing pages should be: Home, About us, Why us, Our Services, Caregiver Resources and Contact Us. Please submit mock up of home page. Company name is TBQ Home Care Agency, logo is attached. Color scheme of the website must be similar to the logo (colors of the Philippine flag).

```html
<!DOCTYPE html>
<html lang="en">
<head>
<meta charset="utf-8">
<title>TBQ Home Care Agency</title>
<link href="https://fonts.googleapis.com/css2?family=Poppins:wght@400;500;600;700&family=Roboto:wght@400;500&display=swap" rel="stylesheet">
<style>
:root{
  --blue:#2e3192;
  --navy:#1b2447;
  --light:#f0f2fa;
  --white:#ffffff;
  --ink:#1f1f2e;
  --muted:#5a5a66;
  --soft:#9a9aa8;
  --yellow:#f5d000;
  --red:#d8262c;
  --footer:#222226;
}
*{margin:0;padding:0;box-sizing:border-box}
html,body{width:1200px;height:2609px;overflow:hidden}
body{position:relative;background:var(--light);font-family:'Roboto',sans-serif;color:var(--ink)}
.abs{position:absolute}
.ph{position:absolute}
h1,h2,h3,h4{font-family:'Poppins',sans-serif;font-weight:500}
p{font-size:13px;line-height:23px}

/* header */
.site-header{left:0;top:0;width:1200px;height:70px;background:var(--white)}
.brand{left:107px;top:14px;display:flex;align-items:center;gap:8px;font-family:'Poppins',sans-serif;font-weight:700;font-size:24px;color:var(--blue)}
.brand-mark{width:14px;height:14px;background:var(--red)}
.nav{top:26px;font-size:12px;color:var(--muted)}
.nav.active{color:var(--blue)}
.btn-apply{left:992px;top:20px;width:101px;height:31px;border:2px solid var(--blue);border-radius:2px;font-size:12px;color:var(--blue);display:flex;align-items:center;justify-content:center}

/* hero */
.hero-kicker{left:107px;top:202px;font-family:'Poppins',sans-serif;font-weight:700;font-size:28px;letter-spacing:4px;color:var(--blue)}
.hero-sub{left:107px;top:234px;font-family:'Poppins',sans-serif;font-size:20px;color:var(--ink)}
.hero-text{left:107px;top:266px;width:480px;color:var(--muted)}
.btn{display:flex;align-items:center;justify-content:center;gap:4px;font-size:12px;font-weight:500}
.btn-contact{left:107px;top:380px;width:124px;height:36px;border:2px solid var(--blue);border-radius:2px;color:var(--ink)}

/* about */
.about-band{left:0;top:504px;width:600px;height:856px;background:var(--blue)}
.label{font-size:11px;letter-spacing:4px;text-transform:uppercase}
.about-label{left:196px;top:843px;color:#d6d8f0}
.about-title{left:196px;top:864px;font-size:26px;font-weight:600;color:var(--white)}
.about-text{left:196px;width:360px;color:#eef0ff}
.btn-read{left:196px;top:1185px;width:123px;height:36px;border:2px solid var(--yellow);border-radius:2px;color:var(--white)}

/* why */
.why-title{left:645px;top:634px;font-size:25px;font-weight:500;color:var(--ink)}
.why-item{left:645px;width:400px;height:80px}
.why-icon{position:absolute;left:0;top:2px;width:53px;height:53px;background:var(--blue);border-radius:3px}
.why-item h3{position:absolute;left:66px;top:0;font-size:16px;color:var(--ink);font-weight:500}
.why-item p{position:absolute;left:66px;top:24px;width:290px;font-size:12px;color:var(--muted)}

/* team */
.team-label{left:107px;top:1405px;color:var(--ink)}
.section-title{font-size:26px;font-weight:600}
.team-title{left:107px;top:1426px;color:var(--ink)}
.member-photo{left:107px;width:177px;height:169px;background:linear-gradient(180deg,var(--blue),#3a3da0)}
.member-card{left:257px;width:272px;height:95px;background:var(--white);padding:12px 14px}
.member-card h4{font-size:14px;font-weight:400;color:var(--ink)}
.member-card .role{font-size:12px;color:var(--soft);margin-top:4px}
.socials{display:flex;gap:12px;margin-top:10px}
.socials span{width:8px;height:8px;border-radius:50%;background:var(--blue)}

/* services */
.services-band{left:600px;top:1360px;width:600px;height:720px;background:var(--blue)}
.svc-label{left:645px;top:1405px;color:#d6d8f0}
.svc-title{left:645px;top:1426px;color:var(--white)}
.svc-photo{left:645px;width:178px;height:118px}
.svc-body{left:836px;width:260px;color:var(--white)}
.svc-body h3{font-size:16px;font-weight:600}
.svc-body p{font-size:12px;line-height:23px;color:#eef0ff;margin-top:4px}

/* contact */
.contact-band{left:107px;top:2080px;width:1093px;height:480px;background:var(--navy)}
.cta-label{left:151px;top:2126px;color:#cfd3e6}
.cta-title{left:151px;top:2142px;color:var(--white)}
.btn-appt{left:877px;top:2140px;width:172px;height:36px;border:2px solid var(--yellow);border-radius:2px;color:var(--white)}
.contact-photo{left:0;top:2216px;width:417px;height:299px;background:linear-gradient(135deg,#c7c2b8,#e6e8ee 55%,#3b6fb5)}
.social-strip{left:373px;top:2336px;width:44px;height:179px;background:var(--yellow);display:flex;flex-direction:column;justify-content:space-around;align-items:center;padding:14px 0}
.social-strip span{width:8px;height:8px;border-radius:50%;background:var(--navy)}
.contact-title{left:444px;top:2213px;font-size:18px;color:var(--white)}
.field{left:444px;width:312px;font-size:12px;color:#b7bdd3;border-bottom:1px solid #3a4466;padding-bottom:12px}
.msg-box{left:444px;top:2356px;width:312px;height:76px;border-bottom:1px solid #3a4466;font-size:12px;color:#b7bdd3}
.btn-submit{left:444px;top:2453px;width:103px;height:35px;border:2px solid var(--yellow);border-radius:2px;color:var(--white)}
.info-box{left:783px;width:310px;height:80px;border:1px solid #2a3456;padding:16px 0 0 50px}
.info-dot{position:absolute;left:14px;top:20px;width:26px;height:26px;border-radius:50%;background:var(--yellow)}
.info-box .k{font-size:10px;color:#8d95b3;text-transform:uppercase}
.info-box .v{font-size:12px;color:var(--white);margin-top:6px}
.hours{left:783px;width:310px;display:flex;justify-content:space-between;font-size:12px;border-bottom:1px solid #2a3456;padding-bottom:10px}
.hours .d{color:#9aa1bd}
.hours .t{color:var(--white)}

/* footer */
.site-footer{left:0;top:2560px;width:1200px;height:49px;background:var(--footer)}
.copy{left:107px;top:2576px;font-size:12px;color:#6f6f78}
.foot-socials{left:990px;top:2580px;display:flex;gap:24px}
.foot-socials span{width:8px;height:8px;border-radius:50%;background:#6f6f78}
</style>
</head>
<body>

<header class="abs site-header">
  <div class="abs brand"><span class="brand-mark"></span>TBQ</div>
  <span class="abs nav active" style="left:564px">Home</span>
  <span class="abs nav" style="left:633px">About Us</span>
  <span class="abs nav" style="left:720px">Our Services</span>
  <span class="abs nav" style="left:825px">Caregiver</span>
  <span class="abs nav" style="left:912px">Contact Us</span>
  <span class="abs btn-apply">Application</span>
</header>

<section class="hero">
  <h1 class="abs hero-kicker">QUALITY CARE</h1>
  <h2 class="abs hero-sub">Your care is our priority</h2>
  <p class="abs hero-text">In publishing and graphic design, lorem ipsum is a placeholder text commonly used to demonstrate the visual form of a document or a typeface without relying In publishing and graphic design, lorem ipsum is a placeholder text commonly used to demonstrate.</p>
  <span class="abs btn btn-contact">Contact Us &#10230;</span>
  <div class="ph" role="img" aria-label="Smiling caregiver in blue scrubs serving tea to an elderly man in a kitchen" style="left:645px;top:70px;width:448px;height:478px;background:linear-gradient(160deg,#c9a77e,#8fa2e0 55%,#e9e6e2)"></div>
</section>

<section class="about">
  <div class="abs about-band"></div>
  <div class="ph" role="img" aria-label="Nurse helping an elderly man walk with a walker" style="left:107px;top:504px;width:493px;height:293px;background:linear-gradient(135deg,#eef0f0,#d8d8d4 50%,#2fb3b0)"></div>
  <span class="abs label about-label">About Us</span>
  <h2 class="abs about-title">Our Story</h2>
  <p class="abs about-text" style="top:910px">In publishing and graphic design, lorem ipsum is a placeholder text commonly used to demonstrate the visual form of a document or a typeface without relying In publishing and graphic design, lorem ipsum is a placeholder text commonly used to demonstrate.</p>
  <p class="abs about-text" style="top:1040px">In publishing and graphic design, lorem ipsum is a placeholder text commonly used to demonstrate the visual form of a document or a typeface without relying In publishing and graphic design, lorem ipsum is a placeholder text commonly used to demonstrate.</p>
  <span class="abs btn btn-read">Read More &#10230;</span>
</section>

<section class="why">
  <h2 class="abs why-title">Why Us</h2>
  <div class="abs why-item" style="top:694px"><span class="why-icon"></span><h3>Free In Home Assessment</h3><p>In publishing and graphic design, lorem ipsum is a placeholder text commonly used to demonstrate.</p></div>
  <div class="abs why-item" style="top:793px"><span class="why-icon"></span><h3>Comfort Match Guarantee</h3><p>In publishing and graphic design, lorem ipsum is a placeholder text commonly used to demonstrate.</p></div>
  <div class="abs why-item" style="top:892px"><span class="why-icon"></span><h3>Bonded and Qualified Caregivers</h3><p>In publishing and graphic design, lorem ipsum is a placeholder text commonly used to demonstrate.</p></div>
  <div class="abs why-item" style="top:991px"><span class="why-icon"></span><h3>24/7 Availability</h3><p>In publishing and graphic design, lorem ipsum is a placeholder text commonly used to demonstrate.</p></div>
  <div class="ph" role="img" aria-label="Video still of a nurse holding hands with an elderly woman" style="left:601px;top:1091px;width:492px;height:269px;background:linear-gradient(120deg,#8fd3c0,#e8e6e2 60%,#f2f2f0)"></div>
  <svg class="abs" style="left:818px;top:1201px" width="52" height="52" viewBox="0 0 52 52"><circle cx="26" cy="26" r="24" fill="none" stroke="#fff" stroke-width="2" opacity=".8"/><path d="M21 17 L35 26 L21 35 Z" fill="#fff"/></svg>
</section>

<section class="team">
  <span class="abs label team-label">Team</span>
  <h2 class="abs section-title team-title">Our Caregivers</h2>
  <div class="ph member-photo" role="img" aria-label="Portrait of a male caregiver in a suit" style="top:1475px"></div>
  <div class="abs member-card" style="top:1549px"><h4>Lorem Ipsum</h4><div class="role">Specialist, TBQ Home Care Agency</div><div class="socials"><span></span><span></span><span></span></div></div>
  <div class="ph member-photo" role="img" aria-label="Portrait of a female caregiver with dark hair" style="top:1671px"></div>
  <div class="abs member-card" style="top:1745px"><h4>Lorem Ipsum</h4><div class="role">Specialist, TBQ Home Care Agency</div><div class="socials"><span></span><span></span><span></span></div></div>
  <div class="ph member-photo" role="img" aria-label="Portrait of a female caregiver with blonde hair" style="top:1868px"></div>
  <div class="abs member-card" style="top:1942px"><h4>Lorem Ipsum</h4><div class="role">Specialist, TBQ Home Care Agency</div><div class="socials"><span></span><span></span><span></span></div></div>
</section>

<section class="services">
  <div class="abs services-band"></div>
  <span class="abs label svc-label">Our Services</span>
  <h2 class="abs section-title svc-title">Services</h2>
  <div class="ph svc-photo" role="img" aria-label="Nurse assisting an elderly woman at home" style="top:1475px;background:linear-gradient(135deg,#d9d2c4,#3b7fd0)"></div>
  <div class="abs svc-body" style="top:1482px"><h3>Companionship</h3><p>In publishing and graphic design, lorem ipsum is a placeholder text commonly used to demonstrate the visual.</p></div>
  <div class="ph svc-photo" role="img" aria-label="Nurse helping an elderly man with a walker" style="top:1620px;background:linear-gradient(135deg,#eceeee,#2fb3b0)"></div>
  <div class="abs svc-body" style="top:1627px"><h3>Home Care Services</h3><p>In publishing and graphic design, lorem ipsum is a placeholder text commonly used to demonstrate the visual.</p></div>
  <div class="ph svc-photo" role="img" aria-label="Caregiver holding hands with an elderly woman" style="top:1765px;background:linear-gradient(135deg,#3a8fd8,#e7d8c8)"></div>
  <div class="abs svc-body" style="top:1772px"><h3>In-Home Care</h3><p>In publishing and graphic design, lorem ipsum is a placeholder text commonly used to demonstrate the visual.</p></div>
  <div class="ph svc-photo" role="img" aria-label="Caregiver serving tea to an elderly man" style="top:1911px;background:linear-gradient(135deg,#c9a77e,#8fa2e0)"></div>
  <div class="abs svc-body" style="top:1918px"><h3>Dementia Care</h3><p>In publishing and graphic design, lorem ipsum is a placeholder text commonly used to demonstrate the visual.</p></div>
</section>

<section class="contact">
  <div class="abs contact-band"></div>
  <span class="abs label cta-label">Get Start</span>
  <h2 class="abs section-title cta-title">Your Care Is Our Priority</h2>
  <span class="abs btn btn-appt">Make An Appointment</span>
  <div class="ph contact-photo" role="img" aria-label="Nurse in blue scrubs caring for an elderly woman beside a wheelchair"></div>
  <div class="abs social-strip"><span></span><span></span><span></span><span></span></div>

  <h3 class="abs contact-title">Contact Us</h3>
  <div class="abs field" style="top:2261px">Enter Name</div>
  <div class="abs field" style="top:2310px">Enter Name</div>
  <div class="abs msg-box" style="padding-top:2px">Message</div>
  <span class="abs btn btn-submit">Submit &#10148;</span>

  <div class="abs info-box" style="top:2213px"><span class="info-dot"></span><div class="k">Email Us</div><div class="v">info@tbqhomecare.example</div></div>
  <div class="abs info-box" style="top:2303px"><span class="info-dot"></span><div class="k">Location</div><div class="v">TBQ Home care agency, USA</div></div>
  <div class="abs hours" style="top:2410px"><span class="d">Monday - Friday</span><span class="t">10am - 5pm</span></div>
  <div class="abs hours" style="top:2449px"><span class="d">Saturday</span><span class="t">10am - 4pm</span></div>
  <div class="abs hours" style="top:2488px"><span class="d">Sunday</span><span class="t">10am - 12pm</span></div>
</section>

<footer class="abs site-footer"></footer>
<span class="abs copy">Copyright &copy; TBQ All rights reserved.</span>
<div class="abs foot-socials"><span></span><span></span><span></span><span></span></div>

</body>
</html>
```